brisk-vale.com Real Estate, Investment, Financial corporate

Real Estate, Investment, Financial corporate looking site. Show present a professional firm, with an elegant display. Please see the attached file which includes the logo, palette and fonts.
Updates

We just starting the brief today. ( logo was delayed)

Target Market(s)

Investors, Corporate , B2b

Industry/Entity Type

real-estate investments

Number of Pages Required

3 page

Requirements
Must have
• Dazzling Homepage
Nice to have
• paralex

```html
<!DOCTYPE html>
<html lang="en">
<head>
<meta charset="utf-8">
<title>Halvard Brisk Vale — Real Estate, Investment, Financial Corporate</title>
<link href="https://fonts.googleapis.com/css2?family=Rubik:ital,wght@0,400;0,500;0,700;0,800;1,400&display=swap" rel="stylesheet">
<style>
  :root{
    --orange:#f05a1a;
    --orange-dark:#d94a0f;
    --ink:#333436;
    --muted:#6f7175;
    --slate:#3b3e43;
    --slate-deep:#2e3135;
    --white:#ffffff;
    --line:#e6e6e6;
  }
  *{box-sizing:border-box;margin:0;padding:0}
  html,body{width:1200px;height:4280px;overflow:hidden}
  body{font-family:"Rubik",sans-serif;color:var(--ink);background:var(--white);position:relative}
  section,header,footer{position:absolute;left:0;width:1200px}
  .abs{position:absolute}
  .center{left:0;width:1200px;text-align:center}
  .accent{color:var(--orange)}
  .btn{position:absolute;background:var(--orange);color:var(--white);font-weight:700;font-size:15px;border-radius:22px;display:flex;align-items:center;justify-content:center;letter-spacing:.3px;text-transform:uppercase}
  .photo{position:absolute}

  /* Hero */
  .hero{top:0;height:712px;overflow:hidden}
  .hero-photo{left:0;top:0;width:1200px;height:712px;background:linear-gradient(120deg,#8a8d90 0%,#b8b6b0 35%,#9a8f7f 60%,#5e5a55 100%)}
  .hero-shade{position:absolute;inset:0;background:rgba(30,32,36,.38)}
  .topbar{position:absolute;top:0;left:0;width:1200px;height:30px;color:var(--white);font-size:13px}
  .topbar .phone{position:absolute;left:60px;top:6px;display:flex;align-items:center;gap:8px}
  .topbar .social{position:absolute;right:62px;top:9px;display:flex;gap:14px}
  .topbar .social span{width:12px;height:12px;border-radius:50%;background:var(--white);opacity:.9}
  .topbar .social span:first-child{background:var(--orange)}
  .navbar{position:absolute;top:30px;left:0;width:1200px;height:50px;background:rgba(70,74,80,.85);border-bottom:1px solid rgba(255,255,255,.25)}
  .nav-item{position:absolute;top:17px;font-size:11px;color:var(--white);text-transform:uppercase;letter-spacing:.3px}
  .nav-item.active{top:10px;background:var(--orange);border-radius:16px;padding:7px 16px}
  .logo{position:absolute;left:523px;top:13px;width:154px;height:74px;background:var(--orange);color:var(--white);font-weight:700;font-size:32px;display:flex;align-items:center;justify-content:center;border-bottom:3px solid var(--white);border-radius:0 0 6px 6px}
  .hero-title{top:288px;font-size:45px;font-weight:800;color:var(--white);letter-spacing:.5px}
  .hero-sub{top:344px;font-size:30px;font-weight:500;color:var(--orange)}
  .hero-tags{left:400px;top:410px;width:414px;height:36px;background:rgba(40,42,46,.6);color:var(--white);font-size:16px;display:flex;align-items:center;justify-content:center;gap:10px}
  .arrow{position:absolute;top:348px;width:36px;height:36px;border:1px solid rgba(255,255,255,.7);border-radius:50%}

  /* Welcome */
  .welcome{top:712px;height:485px;overflow:hidden}
  .tower{left:274px;top:69px;width:226px;height:416px;background:linear-gradient(180deg,#f3f3f3,#e2e2e2)}
  .welcome .kicker{top:76px;font-size:14px}
  .welcome h2{position:absolute;top:100px;font-size:34px;font-weight:700}
  .welcome p{position:absolute;left:375px;width:450px;font-size:11.5px;line-height:20px;color:var(--muted);text-align:center}

  /* Services */
  .services{top:1197px;height:1125px;background:linear-gradient(180deg,#3a3d42 0%,#2f3236 60%,#3b3e43 100%)}
  .sec-title{position:absolute;font-size:34px;font-weight:700}
  .sec-sub{position:absolute;font-size:13px;font-style:italic}
  .services .sec-title{color:var(--white);top:70px}
  .services .sec-sub{color:#d8d8d8;top:122px}
  .card{position:absolute;left:131px;width:938px;height:262px;background:var(--white)}
  .card .photo{top:18px;width:340px;height:225px}
  .card h3{position:absolute;top:64px;font-size:28px;font-weight:500}
  .card p{position:absolute;top:112px;width:370px;font-size:11.5px;line-height:20px;color:var(--muted)}
  .tab{position:absolute;bottom:0;width:130px;height:34px;background:var(--orange);color:var(--white);font-size:13px;font-weight:700;display:flex;align-items:center;justify-content:center}
  .tab.right{right:0;clip-path:polygon(10% 0,100% 0,100% 100%,0 100%)}
  .tab.left{left:0;clip-path:polygon(0 0,90% 0,100% 100%,0 100%)}

  /* Portfolio */
  .portfolio{top:2322px;height:713px}
  .portfolio .sec-title{top:75px}
  .portfolio .sec-sub{top:122px;color:var(--muted)}
  .tile{position:absolute;border-radius:3px}
  .caption{position:absolute;left:0;bottom:0;width:100%;height:50px;display:flex;align-items:center;justify-content:space-between;padding:0 12px 0 24px;color:var(--white);font-size:14px;letter-spacing:.3px;border-bottom:6px solid var(--orange);background:linear-gradient(0deg,rgba(0,0,0,.45),rgba(0,0,0,0))}
  .zoom{width:28px;height:28px;background:var(--orange);border-radius:3px;display:flex;align-items:center;justify-content:center}
  .view-all{position:absolute;font-size:13px;font-weight:700;font-style:italic;color:var(--orange);text-decoration:underline}

  /* CTA */
  .cta{top:3035px;height:359px;overflow:hidden}
  .cta-photo{left:0;top:0;width:1200px;height:359px;background:linear-gradient(100deg,#6e7074 0%,#8b8a88 45%,#56585c 100%)}
  .cta-shade{position:absolute;inset:0;background:rgba(35,37,41,.5)}
  .cta .line1{top:95px;font-size:30px;font-weight:500;color:var(--white)}
  .cta .line2{top:135px;font-size:30px;font-weight:700;color:var(--orange)}
  .cta .line3{top:182px;font-size:15px;font-style:italic;color:var(--white)}

  /* News */
  .news{top:3394px;height:578px}
  .news .sec-title{top:75px}
  .news .sec-sub{top:124px;color:var(--muted)}
  .news-card{position:absolute;left:131px;top:174px;width:938px;height:264px;background:var(--white);box-shadow:0 0 12px rgba(0,0,0,.1)}
  .news-card h4{position:absolute;left:470px;width:390px;top:46px;font-size:15px;font-weight:500;line-height:24px;text-align:center}
  .news-card .date{position:absolute;left:470px;width:390px;top:101px;font-size:12px;color:var(--orange);text-align:center}
  .news-card p{position:absolute;left:470px;width:390px;top:128px;font-size:11px;line-height:19px;color:var(--muted);text-align:center}

  /* Footer */
  .site-footer{top:3972px;height:308px;background:var(--slate);color:var(--white)}
  .col{position:absolute;top:55px}
  .brand{font-size:31px;font-weight:700}
  .col h5{font-size:16px;font-weight:500;margin-bottom:22px}
  .col p,.col li{font-size:12px;line-height:18px;color:#e6e6e6}
  .col ul{list-style:none}
  .col li{margin-bottom:4px;padding-left:22px;position:relative}
  .col li::before{content:"";position:absolute;left:0;top:7px;width:5px;height:5px;border-radius:50%;background:var(--orange)}
  .contact-row{display:flex;gap:14px;margin-bottom:20px}
  .circles{display:flex;gap:8px;margin-top:14px}
  .circles span{width:34px;height:34px;border:2px solid var(--white);border-radius:50%}
  .circles span:first-child{border-color:var(--orange)}
  .copy{position:absolute;top:277px;left:0;width:1200px;text-align:center;font-size:11px;color:#dcdcdc}
</style>
</head>
<body>

<header class="hero">
  <div class="photo hero-photo" role="img" aria-label="Advisor and client reviewing an investment contract with coins and a small house model on the desk"></div>
  <div class="hero-shade"></div>

  <div class="topbar">
    <div class="phone">
      <svg width="20" height="20" viewBox="0 0 20 20"><circle cx="10" cy="10" r="9" fill="none" stroke="#f05a1a" stroke-width="1.5"/><path d="M6.5 5.5l2 0 1 2.5-1.3 1c.6 1.3 1.5 2.2 2.8 2.8l1-1.3 2.5 1v2c-4.5.3-8.3-3.5-8-8z" fill="#f05a1a"/></svg>
      (+1) 555 014 2290
    </div>
    <div class="social"><span></span><span></span><span></span><span></span></div>
  </div>

  <nav class="navbar">
    <span class="nav-item active" style="left:246px">Home</span>
    <span class="nav-item" style="left:336px">About Us</span>
    <span class="nav-item" style="left:425px">Services</span>
    <span class="nav-item" style="left:721px">Portfolio</span>
    <span class="nav-item" style="left:814px">News</span>
    <span class="nav-item" style="left:878px">Contact Us</span>
  </nav>
  <div class="logo">Halvard</div>

  <span class="arrow" style="left:60px"><svg width="34" height="34" viewBox="0 0 34 34"><path d="M19 12l-5 5 5 5" fill="none" stroke="#fff" stroke-width="1.5"/></svg></span>
  <span class="arrow" style="left:1102px"><svg width="34" height="34" viewBox="0 0 34 34"><path d="M15 12l5 5-5 5" fill="none" stroke="#fff" stroke-width="1.5"/></svg></span>

  <h1 class="abs center hero-title">HALVARD REAL ESTATE</h1>
  <div class="abs center hero-sub">INVEST IN YOUR SUCCESS</div>
  <div class="abs hero-tags"><span>Real Estate</span>|<span>Investment</span>|<span>Financial Corporate</span></div>
  <a class="btn" style="left:528px;top:459px;width:142px;height:40px">Get Estimate</a>
</header>

<section class="welcome">
  <div class="photo tower" role="img" aria-label="Faint high-rise apartment tower"></div>
  <div class="abs center kicker">Welcome To</div>
  <h2 class="center">Halvard <span class="accent">Brisk Vale</span></h2>
  <p style="top:156px">Lorem Ipsum is simply dummy text of the printing and typesetting industry. Lorem Ipsum has been the industry's standard dummy text ever since the 1500s, when an unknown printer took a galley of type and scrambled it to make a type specimen book</p>
  <p style="top:246px">It has survived not only five centuries, but also the leap into electronic typesetting, remaining essentially unchanged. It was popularised in the 1960s with the release of Letraset sheets containing Lorem Ipsum passages, and more recently with desktop publishing software like Aldus PageMaker including versions of Lorem Ipsum Lorem Ipsum is simply dummy printing.</p>
  <a class="btn" style="left:528px;top:368px;width:142px;height:40px">Learn More</a>
</section>

<section class="services">
  <h2 class="sec-title center">Services <span class="accent">We Provide</span></h2>
  <div class="sec-sub center">Lorem Ipsum is simply dummy text of the printing and typesetting industry.</div>

  <article class="card" style="top:181px">
    <div class="photo" style="left:19px;background:linear-gradient(135deg,#7d8894,#c9ccd0 50%,#8e8a84)" role="img" aria-label="Hand pointing a pen at an architectural building model"></div>
    <h3 style="left:467px">Real Estate</h3>
    <p style="left:467px">Lorem Ipsum is simply dummy text of the printing and typesetting industry. Lorem Ipsum has been the industry's standard dummy text ever since the 1500s, when an unknown printer took a galley of type and scrambled it to make a type specimen book</p>
    <span class="tab right">LEARN MORE</span>
  </article>

  <article class="card" style="top:483px">
    <h3 style="left:63px">Investment</h3>
    <p style="left:63px">Lorem Ipsum is simply dummy text of the printing and typesetting industry. Lorem Ipsum has been the industry's standard dummy text ever since the 1500s, when an unknown printer took a galley of type and scrambled it to make a type specimen book</p>
    <div class="photo" style="left:578px;background:linear-gradient(160deg,#1f3550,#3a5a7c 55%,#c89a5e)" role="img" aria-label="Stacks of coins with a rising financial chart"></div>
    <span class="tab left">LEARN MORE</span>
  </article>

  <article class="card" style="top:787px">
    <div class="photo" style="left:19px;background:linear-gradient(135deg,#d8dadc,#9ea3a8 50%,#4d5156)" role="img" aria-label="Business team in a meeting room reviewing a presentation chart"></div>
    <h3 style="left:467px">Financial Corporate</h3>
    <p style="left:467px">Lorem Ipsum is simply dummy text of the printing and typesetting industry. Lorem Ipsum has been the industry's standard dummy text ever since the 1500s, when an unknown printer took a galley of type and scrambled it to make a type specimen book</p>
    <span class="tab right">LEARN MORE</span>
  </article>
</section>

<section class="portfolio">
  <h2 class="sec-title center">Work <span class="accent">Portfolio</span></h2>
  <div class="sec-sub center">Lorem Ipsum is simply dummy text of the printing and typesetting industry.</div>

  <div class="tile" style="left:113px;top:176px;width:145px;height:153px;background:linear-gradient(160deg,#9fb0bf,#5c5a55)" role="img" aria-label="Modern two-storey villa"></div>
  <div class="tile" style="left:278px;top:176px;width:146px;height:153px;background:linear-gradient(160deg,#cfe0ee,#b8a68c 60%,#6d8a4c)" role="img" aria-label="Suburban family house"></div>
  <div class="tile" style="left:445px;top:176px;width:311px;height:239px;background:linear-gradient(170deg,#7fa3c6,#9aa3ab 60%,#4e5a4a);overflow:hidden" role="img" aria-label="High-rise residential tower">
    <div class="caption"><span>LOREM IPSUM SIMPLE TEXT</span><span class="zoom"><svg width="16" height="16" viewBox="0 0 16 16"><circle cx="7" cy="7" r="4.5" fill="none" stroke="#fff" stroke-width="1.6"/><path d="M10.5 10.5l3.5 3.5M5 7h4M7 5v4" stroke="#fff" stroke-width="1.6"/></svg></span></div>
  </div>
  <div class="tile" style="left:778px;top:176px;width:144px;height:153px;background:linear-gradient(160deg,#5a7fa8,#b07a4e 60%,#3d4a5a)" role="img" aria-label="Contemporary house at dusk"></div>
  <div class="tile" style="left:942px;top:176px;width:147px;height:153px;background:linear-gradient(160deg,#4e7fc0,#9a7b5e 60%,#5f7a48)" role="img" aria-label="Single-storey brick home"></div>
  <div class="tile" style="left:113px;top:350px;width:311px;height:238px;background:linear-gradient(160deg,#b9c9d6,#b8503e 50%,#6a8a4a)" role="img" aria-label="Row of colourful townhouses"></div>
  <div class="tile" style="left:445px;top:438px;width:311px;height:150px;background:linear-gradient(170deg,#a9c3da,#c9c6bf 55%,#6d6f70)" role="img" aria-label="Modern duplex houses along a street"></div>
  <div class="tile" style="left:778px;top:350px;width:311px;height:238px;background:linear-gradient(170deg,#8fb3d8,#4f7fa3 50%,#7a8a4e)" role="img" aria-label="Blue coastal houses on a hillside"></div>

  <a class="view-all center" style="top:622px">VIEW ALL WORK</a>
</section>

<section class="cta">
  <div class="photo cta-photo" role="img" aria-label="Couple meeting with an agent in a bright office"></div>
  <div class="cta-shade"></div>
  <div class="abs center line1">NEED AN HAVE ANY QUESTION or</div>
  <div class="abs center line2">REAL ESTATE SERVICES HELP ?</div>
  <div class="abs center line3">Lorem Ipsum has been the industry's standard dummy Text.</div>
  <a class="btn" style="left:528px;top:231px;width:142px;height:40px">Contact Us</a>
</section>

<section class="news">
  <h2 class="sec-title center">Latest <span class="accent">News</span></h2>
  <div class="sec-sub center">Lorem Ipsum is simply dummy text of the printing and typesetting industry.</div>
  <article class="news-card">
    <div class="photo" style="left:19px;top:20px;width:340px;height:225px;background:linear-gradient(135deg,#e4e4e2,#a9a7a2 55%,#5b4a3e)" role="img" aria-label="Couple looking at property listings in an agency window"></div>
    <h4>Lorem Ipsum is simply dummy text of the printing and typesetting industry.</h4>
    <div class="date">10 August 2021 &nbsp;| By Halvard Brisk Vale</div>
    <p>Lorem Ipsum is simply dummy text of the printing and typesetting industry. Lorem Ipsum has been the industry's standard dummy text ever since the 1500s, when an unknown printer took</p>
    <a class="btn" style="left:595px;top:197px;width:142px;height:40px">Learn More</a>
  </article>
  <a class="view-all center" style="top:486px">VIEW ALL WORK</a>
</section>

<footer class="site-footer">
  <div class="col" style="left:60px;top:45px;width:220px">
    <div class="brand">Halvard</div>
    <p style="margin-top:10px">If you have an any Question for<br>contact us Today !</p>
    <a class="btn" style="position:relative;width:142px;height:38px;margin-top:12px;font-size:14px">Get Estimate</a>
    <div class="circles"><span></span><span></span><span></span><span></span></div>
  </div>

  <div class="col" style="left:337px;width:240px">
    <h5>Contact <span class="accent">Us</span></h5>
    <div class="contact-row">
      <svg width="20" height="20" viewBox="0 0 20 20"><path d="M10 1a6 6 0 0 0-6 6c0 4.5 6 12 6 12s6-7.5 6-12a6 6 0 0 0-6-6z" fill="#f05a1a"/><circle cx="10" cy="7" r="2.2" fill="#3b3e43"/></svg>
      <p><span class="accent">Halvard Brisk Vale</span><br>42 Vale Street, Suite 300,<br>Harbor District</p>
    </div>
    <div class="contact-row" style="align-items:center">
      <svg width="20" height="20" viewBox="0 0 20 20"><path d="M4 3l3 0 1.5 3.5-2 1.5c1 2 2.5 3.5 4.5 4.5l1.5-2 3.5 1.5v3c-6.5.5-12.5-5.5-12-12z" fill="none" stroke="#f05a1a" stroke-width="1.5"/></svg>
      <p style="font-size:15px">555 014 2290</p>
    </div>
    <div class="contact-row" style="align-items:center">
      <svg width="20" height="16" viewBox="0 0 20 16"><rect x="1" y="1" width="18" height="14" fill="none" stroke="#f05a1a" stroke-width="1.5"/><path d="M1 1l9 7 9-7" fill="none" stroke="#f05a1a" stroke-width="1.5"/></svg>
      <p>info@halvard-vale.com</p>
    </div>
  </div>

  <div class="col" style="left:612px;width:220px">
    <h5>Quick <span class="accent">Links</span></h5>
    <ul><li>Home</li><li>About</li><li>Services</li><li>Portfolio</li><li>News</li><li>Contact Us</li></ul>
  </div>

  <div class="col" style="left:888px;width:240px">
    <h5>Our <span class="accent">Services</span></h5>
    <ul><li>Real Estate</li><li>Investment</li><li>Financial Corporate</li></ul>
  </div>

  <div class="copy">©<span class="accent">Halvard Brisk Vale</span> - 2021 All rights reserved.</div>
</footer>

</body>
</html>
```